Business Cards

I'm an contractor and consultant in IT Project management. I'd like a design for business cards.
In my work I mostly meet clients, peer project managers and technical staff. I usually exchange business cards at technical conventions or when networking.
I provide services that are:
- Updated, always with a fresh look on technology
- Solid and reliable
- Flexible schedule and always available
The current business card has been attached to provide information.
Target Market(s)
IT managers, IT project managers, consultants, recruitment staff. Age 30-45 years. College/University degree.
Industry/Entity Type
Contractor
Colors
Designer to choose colors to be used in the design.
Requirements
Must have
- Two sides, one side with personal information and the other side with company name.
Text in Norwegian, including Norwegian characters
Nice to have
- It should be possible for non-Norwegian speakers to read the contact details.

```html
<!DOCTYPE html>
<html lang="no">
<head>
<meta charset="utf-8">
<title>Molvik Consulting AS – visittkort</title>
<link href="https://fonts.googleapis.com/css2?family=Cinzel:wght@500&family=PT+Sans:wght@400;700&family=Sorts+Mill+Goudy&display=swap" rel="stylesheet">
<style>
  :root {
    --paper: #ffffff;
    --ink: #1f1f1f;
    --band: #0a2a5c;
    --band-deep: #072350;
    --band-motif: #0d3470;
    --band-text: #ffffff;
  }
  html, body {
    margin: 0;
    padding: 0;
    width: 1200px;
    height: 741px;
    overflow: hidden;
    background: var(--paper);
  }
  .card {
    position: relative;
    width: 1200px;
    height: 741px;
    background: var(--paper);
  }
  .holder-name {
    position: absolute;
    right: 84px;
    top: 58px;
    margin: 0;
    font-family: "Cinzel", serif;
    font-weight: 500;
    font-size: 40px;
    letter-spacing: 1px;
    color: var(--ink);
  }
  .contact {
    position: absolute;
    left: 83px;
    top: 408px;
    margin: 0;
    font-family: "PT Sans", sans-serif;
    font-size: 32px;
    line-height: 41px;
    color: var(--ink);
    font-style: normal;
  }
  .contact .strong { font-weight: 700; }
  .company-band {
    position: absolute;
    left: 485px;
    top: 387px;
    width: 715px;
    height: 248px;
    background: var(--band);
    border-radius: 11px 0 0 11px;
    overflow: hidden;
  }
  .band-motif {
    position: absolute;
    inset: 0;
    background:
      radial-gradient(ellipse 260px 200px at 62% 20%, var(--band-motif), transparent 70%),
      radial-gradient(ellipse 200px 180px at 95% 75%, var(--band-motif), transparent 70%),
      linear-gradient(90deg, var(--band) 0%, var(--band-deep) 100%);
  }
  .company {
    position: absolute;
    right: 121px;
    top: 38px;
    text-align: right;
    color: var(--band-text);
  }
  .company-name {
    margin: 0;
    font-family: "Cinzel", serif;
    font-weight: 500;
    font-size: 43px;
    line-height: 1.1;
  }
  .company-tagline {
    margin: 8px 0 0;
    font-family: "Sorts Mill Goudy", serif;
    font-size: 31px;
    line-height: 1.1;
  }
</style>
</head>
<body>
  <main class="card">
    <h1 class="holder-name">Even Molvik</h1>

    <address class="contact">
      Thorvalds gate 14<br>
      <span class="strong">Oslo 0461</span><br>
      Mobil: <span class="strong">41582096</span><br>
      even@molvikconsulting.no<br>
      www.molvikconsulting.no
    </address>

    <section class="company-band">
      <div class="band-motif" role="img" aria-label="Dekorativt blomster- og rankemønster i mørkeblått"></div>
      <div class="company">
        <p class="company-name">Molvik Consulting AS</p>
        <p class="company-tagline">IT Implementering</p>
      </div>
    </section>
  </main>
</body>
</html>
```